Spring 2026 Deck Construction Direct Mail Flier

The logo files I will include were named "maple ridge fixers" by the digital artist. However, my company is called Maple Ridge Yardworks (That was not a typo. There is no space between "home" and "service") If you'd like to experiment with color modification of the logo to make it fit better with designs you come up with, please be my guest.

I need a 6"x12" flier design to market my deck construction business. The expected goal is to get phone calls and book appointments for the upcoming Spring 2026 construction season. The call to action being something along the lines of "Call now; Appointments are going fast!"

My target audience is upper middle class (annual household income $100,000 - $200,000) families of 3-5 in the capital region of New York state, US. Houses are most commonly either vinyl sided, or sometimes a combination of vinyl siding and brick. The ideal flier design will feature this type of house. Also most houses in my target area have nice lawns with mulched gardens as well.

I prefer designs with more sweeping, gradual curves than sharp square edges and corners, though some squares and corners are ok. I like designs with pallets consisting of blue, red, green, black, gray. I do not like purple, pink, yellow, or orange.

If it's possible and will fit, it would be nice to have images of pressure treated lumber, western cedar decking, and composite decking, so that customers understand I can provide any of the three. Also listing them out would be great.

I prefer designs that are more visual than text-based. On at least one side the dominant element should be a visual of a large composite or cedar deck. An image somewhere - wherever it can fit - of a small (10'x14' or so), basic deck of pressure treated lumber would be ideal as well so that potential clients know I will build those. Also I would like some element, on either side, that creates a sense of urgency by drawing the eye to text along the lines of "2026 appointments are filling fast. Book your free consultation today!"

Selling points:
- Veteran owned and operated
- Hometown feel
- Personal service
- Satisfaction guaranteed

I will use the Northfield Parcel Bureau's "Bright Lane Route Mailer" (BLRM) service to deliver these, so on either the front or back there should be a small amount of reserved space in the top right corner for the NFPB's required markings (see https://www.larkstonepromo.com/products/plumber-fixit-blrm-postcard?variant=17305529816 for an example of the amount of space required). It's ok if there is imagery there and it gets covered up by the NFPB markings, it just shouldn't be anything important. You do not have to include the NFPB markings themselves. My print guy will do that when I pass him this design.

A final note on this; I've mentioned Spring 2026 several times. But I do not want the design to be relevant only for Spring. I'd like to use the design throughout the year so please no hard references to Spring that will make the flier seem out of place in the fall.

Thank you very much. I appreciate your time.

```html
<!DOCTYPE html>
<html lang="en">
<head>
<meta charset="utf-8">
<title>Maple Ridge Yardworks – Deck Mailer</title>
<link rel="stylesheet" href="https://fonts.googleapis.com/css2?family=Montserrat:wght@400;500;600;700;800;900&family=Playfair+Display:ital,wght@0,400;0,500;1,400&display=swap">
<style>
  :root{
    --navy:#132a52;
    --navy-deep:#0f2447;
    --red:#a8202e;
    --white:#ffffff;
    --ink:#111111;
    --page:#f3f3f3;
    --label-gray:#c3b8b1;
    --sans:"Montserrat", Arial, sans-serif;
    --serif:"Playfair Display", Georgia, serif;
  }
  *{box-sizing:border-box;margin:0;padding:0}
  html,body{width:1200px;height:1137px;overflow:hidden;background:var(--page)}
  .canvas{position:relative;width:1200px;height:1137px}
  .card{position:absolute;left:150px;background:var(--white);overflow:hidden}
  .card--front{top:57px;width:905px;height:491px}
  .card--back{top:596px;width:902px;height:491px}
  .shapes{position:absolute;inset:0;width:100%;height:100%}
  .photo{position:absolute}

  /* front */
  .photo--hero{left:180px;top:0;width:725px;height:340px;
    background:linear-gradient(180deg,#dcdcd8 0%,#eeeeea 35%,#c9a27a 60%,#8a4a22 85%,#6b3517 100%)}
  .brand-seal{position:absolute;display:flex;align-items:center;justify-content:center;text-align:center;
    background:var(--white);border-radius:50%;font-family:var(--sans);font-weight:800;color:var(--navy);
    text-transform:uppercase;line-height:1.15}
  .card--front .brand-seal{left:27px;top:48px;width:146px;height:146px;font-size:16px;padding:18px}
  .headline{position:absolute;right:28px;top:18px;text-align:right;color:var(--white)}
  .headline__main{font-family:var(--sans);font-weight:900;font-size:50px;letter-spacing:.5px;line-height:1.1}
  .headline__sub{font-family:var(--serif);font-style:italic;font-size:36px;line-height:1.1;margin-top:2px}
  .cta{position:absolute;left:26px;top:268px}
  .cta__call{font-family:var(--serif);color:var(--red);font-size:62px;line-height:1}
  .cta__offer{font-family:var(--sans);font-weight:800;color:var(--navy);font-size:37px;line-height:1;margin-top:14px}
  .cta__urgency{font-family:var(--sans);font-weight:700;color:var(--ink);font-size:21px;margin-top:5px}
  .phone{display:flex;align-items:center;font-family:var(--sans);font-weight:800;color:var(--ink)}
  .phone__icon{flex:none;border-radius:50%;background:var(--red);display:flex;align-items:center;justify-content:center;border:2px solid #fff;box-shadow:0 0 0 2px var(--red)}
  .cta .phone{margin-top:14px;font-size:48px;gap:14px}
  .cta .phone__icon{width:46px;height:46px}
  .materials{position:absolute;left:482px;top:351px;font-family:var(--sans);font-weight:500;font-size:15px;color:var(--navy);white-space:nowrap}
  .materials .sep{color:var(--red);margin:0 7px}
  .perks{position:absolute;left:480px;top:384px;display:grid;grid-template-columns:196px 196px;gap:7px 8px}
  .perk{height:43px;background:var(--navy);border-radius:3px;display:flex;align-items:center;gap:10px;padding-left:14px;
    color:var(--white);font-family:var(--sans);font-weight:500;font-size:13px;line-height:1.1}
  .perk svg{flex:none}

  /* back */
  .photo--patio{left:0;top:0;width:600px;height:300px;
    background:linear-gradient(180deg,#8fa9c9 0%,#c3cfdc 30%,#b9b9b6 55%,#7d7f80 80%,#5f6b4a 100%)}
  .card--back .brand-seal{left:424px;top:46px;width:166px;height:166px;font-size:18px;padding:20px}
  .services{position:absolute;left:27px;top:262px;color:var(--white);font-family:var(--sans)}
  .services__title{font-weight:700;font-size:27px;line-height:1.25}
  .services__list{list-style:none;margin-top:16px;font-size:15px;font-weight:400}
  .services__list li{display:flex;align-items:center;gap:7px;height:23px}
  .photo--build{left:285px;top:354px;width:169px;height:104px;
    background:linear-gradient(160deg,#6a6e70 0%,#c49a6a 45%,#a9763f 100%)}
  .divider{position:absolute;left:505px;top:343px;width:1.5px;height:117px;background:rgba(255,255,255,.8)}
  .contact{position:absolute;left:534px;top:340px;color:var(--white);font-family:var(--sans)}
  .contact__lead{font-weight:700;font-size:17px;line-height:1.2}
  .contact__book{font-weight:400;font-size:16px;line-height:1.2}
  .contact .phone{color:var(--white);font-size:38px;gap:10px;margin-top:10px}
  .contact .phone__icon{width:38px;height:38px;border-color:#fff;box-shadow:0 0 0 2px var(--red)}
  .contact__line{font-size:13px;font-weight:500;margin-top:3px}
  .contact__line:first-of-type{margin-top:6px}
  .stamp{position:absolute;left:804px;top:23px;width:73px;height:73px;background:var(--label-gray);color:#fff;
    font-family:Arial, sans-serif;font-size:8px;text-align:center}
  .stamp__text{position:absolute;left:0;right:0;top:26px;line-height:1.2}
  .label-area{position:absolute;left:692px;top:126px;width:186px;height:63px;background:var(--label-gray);color:#fff;
    font-family:Arial, sans-serif;text-align:center}
  .label-area__size{font-size:8px;font-weight:700;margin-top:4px}
  .label-area__note{font-size:6px;line-height:1.2;margin:2px 22px 0 14px}
  .label-area__title{font-size:10px;font-weight:700;margin-top:2px}
  .label-area__height{position:absolute;right:2px;top:10px;font-size:7px;font-weight:700;writing-mode:vertical-rl}
</style>
</head>
<body>
<main class="canvas">

  <!-- FRONT -->
  <section class="card card--front" aria-label="Mailer front">
    <div class="photo photo--hero" role="img" aria-label="Large wooden deck flowing into a bright open-plan living space"></div>
    <svg class="shapes" viewBox="0 0 905 491" preserveAspectRatio="none" aria-hidden="true">
      <path d="M0,0 H215 C185,80 195,170 250,262 L0,270 Z" fill="var(--navy)"/>
      <path d="M0,246 C260,224 520,258 905,318 V491 H0 Z" fill="var(--red)"/>
      <path d="M0,254 C260,234 520,268 905,330 V491 H0 Z" fill="var(--white)"/>
    </svg>
    <div class="brand-seal">Maple Ridge Yardworks</div>
    <div class="headline">
      <p class="headline__main">YOUR DREAM DECK</p>
      <p class="headline__sub">Built for How You Live</p>
    </div>
    <div class="cta">
      <p class="cta__call">Call Now</p>
      <p class="cta__offer">FREE CONSULTATION</p>
      <p class="cta__urgency">2026 Appointments Are Filling Fast!</p>
      <p class="phone">
        <span class="phone__icon"><svg width="20" height="20" viewBox="0 0 24 24"><path fill="#fff" d="M6.6 10.8a15.1 15.1 0 0 0 6.6 6.6l2.2-2.2a1 1 0 0 1 1-.25 11.4 11.4 0 0 0 3.6.57 1 1 0 0 1 1 1V20a1 1 0 0 1-1 1A17 17 0 0 1 3 4a1 1 0 0 1 1-1h3.5a1 1 0 0 1 1 1c0 1.25.2 2.45.57 3.57a1 1 0 0 1-.25 1z"/></svg></span>
        (518) 555-0147
      </p>
    </div>
    <p class="materials">Pressure Treated<span class="sep">|</span>Western Red Cedar<span class="sep">|</span>Composite</p>
    <div class="perks">
      <div class="perk">
        <svg width="22" height="26" viewBox="0 0 22 26" fill="none" stroke="#fff" stroke-width="2"><path d="M6 1 V9 L11 12 L16 9 V1"/><path d="M11 14 l2.2 4.4 4.8.7-3.5 3.4.8 4.8-4.3-2.3-4.3 2.3.8-4.8-3.5-3.4 4.8-.7z" fill="#fff" stroke="none"/></svg>
        <span>Veteran Owned<br>&amp; Operated</span>
      </div>
      <div class="perk">
        <svg width="24" height="24" viewBox="0 0 24 24" fill="none" stroke="#fff" stroke-width="2"><path d="M12 22s-7-7-7-12a7 7 0 0 1 14 0c0 5-7 12-7 12z"/><path d="M9 12V9l3-2 3 2v3z"/></svg>
        <span>Hometown<br>Craftsmanship</span>
      </div>
      <div class="perk">
        <svg width="28" height="22" viewBox="0 0 28 22" fill="#fff"><circle cx="6" cy="8" r="3.5"/><circle cx="22" cy="8" r="3.5"/><path d="M0 21c0-4 2.5-7 6-7s6 3 6 7zM16 21c0-4 2.5-7 6-7s6 3 6 7z"/><path d="M11 4l3-3 3 3-3 3z"/></svg>
        <span>Personal<br>1-on-1 Service</span>
      </div>
      <div class="perk">
        <svg width="24" height="24" viewBox="0 0 24 24" fill="none" stroke="#fff" stroke-width="2"><path d="M12 2l2.9 6.3 6.9.8-5.1 4.7 1.4 6.8L12 17.2 5.9 20.6l1.4-6.8L2.2 9.1l6.9-.8z"/><path d="M8.5 12l2.5 2.5 4.5-4.5"/></svg>
        <span>Satisfaction<br>Guaranteed</span>
      </div>
    </div>
  </section>

  <!-- BACK -->
  <section class="card card--back" aria-label="Mailer back">
    <div class="photo photo--patio" role="img" aria-label="Gray composite deck with cable railing beside a white-trimmed home and planted garden"></div>
    <svg class="shapes" viewBox="0 0 902 491" preserveAspectRatio="none" aria-hidden="true">
      <path d="M430,0 H902 V320 H600 C520,220 460,120 430,0 Z" fill="var(--white)"/>
      <path d="M0,212 C180,182 380,200 520,250 C640,292 780,286 902,266 V491 H0 Z" fill="var(--navy-deep)"/>
    </svg>
    <div class="brand-seal">Maple Ridge Yardworks</div>

    <div class="stamp">
      <svg class="shapes" viewBox="0 0 73 73" aria-hidden="true" stroke="#fff" stroke-width="1"><path d="M8 8 V48 M5 11 L8 8 L11 11 M5 45 L8 48 L11 45"/><path d="M28 64 H66 M31 61 L28 64 L31 67 M63 61 L66 64 L63 67"/></svg>
      <p class="stamp__text">Stamp<br>1 inch</p>
    </div>
    <div class="label-area">
      <p class="label-area__size">2.5" inch</p>
      <p class="label-area__note">This area needs to remain BLANK WHITE for the BLRM label. Please DO NOT place any graphics, color or text in this area.</p>
      <p class="label-area__title">Label Marking Area</p>
      <p class="label-area__height">.85" inch</p>
    </div>

    <div class="services">
      <h2 class="services__title">Decks Designed Around<br>Your Home &amp; Budget</h2>
      <ul class="services__list">
        <li><svg width="11" height="9" viewBox="0 0 11 9"><path d="M1 4.5l3 3 6-6" fill="none" stroke="#fff" stroke-width="1.6"/></svg>New deck construction</li>
        <li><svg width="11" height="9" viewBox="0 0 11 9"><path d="M1 4.5l3 3 6-6" fill="none" stroke="#fff" stroke-width="1.6"/></svg>Deck replacements</li>
        <li><svg width="11" height="9" viewBox="0 0 11 9"><path d="M1 4.5l3 3 6-6" fill="none" stroke="#fff" stroke-width="1.6"/></svg>Multi-level &amp; attached decks</li>
        <li><svg width="11" height="9" viewBox="0 0 11 9"><path d="M1 4.5l3 3 6-6" fill="none" stroke="#fff" stroke-width="1.6"/></svg>Entry &amp; backyard platforms</li>
        <li><svg width="11" height="9" viewBox="0 0 11 9"><path d="M1 4.5l3 3 6-6" fill="none" stroke="#fff" stroke-width="1.6"/></svg>Custom railings &amp; stairs</li>
      </ul>
    </div>
    <div class="photo photo--build" role="img" aria-label="Builder fastening pressure treated deck boards with a drill"></div>
    <div class="divider"></div>
    <div class="contact">
      <p class="contact__lead">Don’t wait — build season fills quickly.</p>
      <p class="contact__book">Book your FREE consultation today.</p>
      <p class="phone">
        <span class="phone__icon"><svg width="17" height="17" viewBox="0 0 24 24"><path fill="#fff" d="M6.6 10.8a15.1 15.1 0 0 0 6.6 6.6l2.2-2.2a1 1 0 0 1 1-.25 11.4 11.4 0 0 0 3.6.57 1 1 0 0 1 1 1V20a1 1 0 0 1-1 1A17 17 0 0 1 3 4a1 1 0 0 1 1-1h3.5a1 1 0 0 1 1 1c0 1.25.2 2.45.57 3.57a1 1 0 0 1-.25 1z"/></svg></span>
        (518) 555-0147
      </p>
      <p class="contact__line">hello@mapleridgeyardworks.com</p>
      <p class="contact__line">mapleridgeyardworks.com</p>
    </div>
  </section>

</main>
</body>
</html>
```